Professionelles Social Media Material für Reinigungsdienstleister
Zielgruppe
Wir reinigen Privathaushalte, Ferienwohnungen, Arztpraxen und Büroräume.
Aufgabenstellung
Ich wünsche Material für ein professionelles Auftreten bei Facebook und Instagram. Wir müssen bei Facebook leider neu starten und haben Instagram bei dieser Firma bisher vernachlässigt.
Nun wollen wir unser Social Media professionell erscheinen lassen und einen Plan für die kommenden 2 Monate erstellen. Wir suchen dafür mindestens 20 passende Postings und die Inhalte für den Start.
Nachtrag zu den Postings: Wir wollen ganz allgemeinen Content und sind offen für alle Vorschläge. Es kann gern auch eine Sommeraktion beworben werden, bei der wir Neukunden 100€ schenken und eine Aktion, bei der es eine kostenlose Erstreinigung gibt um unsere Leistung zu testen.

```html
<!DOCTYPE html>
<html lang="de">
<head>
<meta charset="utf-8">
<title>Wohnglanz Pilot – Sommeraktion</title>
<link rel="stylesheet" href="https://fonts.googleapis.com/css2?family=Roboto:wght@400;500;700;900&display=swap">
<style>
  :root {
    --navy: #4a5b8c;
    --sky: #49a6c4;
    --ink: #454545;
    --paper: #ffffff;
    --photo-light: #f4f6f8;
    --photo-mid: #dfe3e6;
  }
  * { margin: 0; padding: 0; box-sizing: border-box; }
  html, body { width: 1200px; height: 1200px; overflow: hidden; background: var(--paper); }
  body { font-family: "Roboto", Arial, sans-serif; }
  .post { position: relative; width: 1200px; height: 1200px; background: var(--paper); }

  .brand {
    position: absolute; left: 92px; top: 104px; width: 168px;
    display: flex; flex-direction: column; align-items: center; gap: 14px;
  }
  .brand-dot { width: 96px; height: 96px; border-radius: 50%; background: var(--sky); }
  .brand-name {
    color: var(--navy); font-weight: 700; font-size: 33px; line-height: 40px; text-align: center;
  }

  .headline {
    position: absolute; left: 316px; top: 108px;
    color: var(--navy); font-weight: 900; font-size: 96px; line-height: 98px; letter-spacing: 1px;
  }

  .photo {
    position: absolute; left: 16px; top: 283px; width: 1153px; height: 645px;
    background: radial-gradient(ellipse at 50% 55%, var(--photo-mid) 0%, var(--photo-light) 55%, rgba(255,255,255,0) 78%);
  }

  .badge { position: absolute; left: 889px; top: 392px; width: 242px; height: 242px; }

  .benefits {
    position: absolute; left: 88px; top: 930px; list-style: none;
    color: var(--ink); font-size: 31px; font-weight: 400;
  }
  .benefits li { display: flex; align-items: center; height: 66px; }
  .benefits svg { width: 28px; height: 24px; margin-right: 20px; }

  .offer-tag {
    position: absolute; left: 782px; top: 918px; width: 266px; height: 60px;
    background: var(--navy); color: #fff; border-radius: 12px 12px 0 0;
    font-weight: 500; font-size: 24px; display: flex; align-items: center; justify-content: center;
  }
  .cta {
    position: absolute; left: 693px; top: 977px; width: 445px; height: 98px;
    background: var(--sky); color: #fff; border-radius: 6px;
    box-shadow: 3px 4px 6px rgba(0,0,0,0.35);
    font-weight: 700; font-size: 37px; display: flex; align-items: center; justify-content: center;
  }
  .web {
    position: absolute; left: 693px; top: 1102px; width: 460px; text-align: center;
    color: var(--navy); font-weight: 700; font-size: 22px;
  }
</style>
</head>
<body>
<main class="post">
  <div class="brand">
    <div class="brand-dot"></div>
    <div class="brand-name">Wohnglanz<br>Pilot</div>
  </div>

  <h1 class="headline">SOMMER, SONNE,<br>SAUBERKEIT</h1>

  <div class="photo" role="img" aria-label="Foto einer Familie mit zwei Kindern auf einem weißen Sofa in einem hellen, sauberen Wohnzimmer"></div>

  <svg class="badge" viewBox="0 0 242 242" aria-label="Nur im Sommer – 100 € jetzt sparen">
    <defs>
      <linearGradient id="badgeFill" x1="0" y1="0" x2="1" y2="1">
        <stop offset="0" stop-color="#4aa3c6"/>
        <stop offset="1" stop-color="#4d5f8e"/>
      </linearGradient>
      <path id="arcTop" d="M 36 121 A 85 85 0 0 1 206 121"/>
      <path id="arcBottom" d="M 30 121 A 91 91 0 0 0 212 121"/>
    </defs>
    <circle cx="121" cy="121" r="121" fill="url(#badgeFill)"/>
    <circle cx="121" cy="121" r="110" fill="none" stroke="#fff" stroke-width="3"/>
    <text font-family="Roboto, Arial, sans-serif" font-weight="700" font-size="17" fill="#fff" letter-spacing="3">
      <textPath href="#arcTop" startOffset="50%" text-anchor="middle">NUR IM SOMMER!</textPath>
    </text>
    <text font-family="Roboto, Arial, sans-serif" font-weight="700" font-size="17" fill="#fff" letter-spacing="3">
      <textPath href="#arcBottom" startOffset="50%" text-anchor="middle" dominant-baseline="hanging">JETZT SPAREN</textPath>
    </text>
    <text x="112" y="148" text-anchor="middle" font-family="Roboto, Arial, sans-serif" font-weight="700" font-size="78" fill="#fff">100</text>
    <text x="190" y="150" text-anchor="middle" font-family="Roboto, Arial, sans-serif" font-weight="700" font-size="38" fill="#fff">€</text>
    <text x="188" y="113" text-anchor="middle" font-family="Roboto, Arial, sans-serif" font-weight="700" font-size="22" fill="#fff">*</text>
  </svg>

  <ul class="benefits">
    <li><svg viewBox="0 0 28 24"><path d="M3 12 L11 20 L25 4" fill="none" stroke="#49a6c4" stroke-width="5" stroke-linecap="round" stroke-linejoin="round"/></svg>Zuverlässige Reinigungskräfte</li>
    <li><svg viewBox="0 0 28 24"><path d="M3 12 L11 20 L25 4" fill="none" stroke="#49a6c4" stroke-width="5" stroke-linecap="round" stroke-linejoin="round"/></svg>Flexible Terminwahl</li>
    <li><svg viewBox="0 0 28 24"><path d="M3 12 L11 20 L25 4" fill="none" stroke="#49a6c4" stroke-width="5" stroke-linecap="round" stroke-linejoin="round"/></svg>100 % Zufriedenheitsgarantie</li>
  </ul>

  <div class="offer-tag">Nur für kurze Zeit!</div>
  <div class="cta">Jetzt Angebot sichern</div>
  <div class="web">wohnglanz-pilot-example.de</div>
</main>
</body>
</html>
```